Buisness Card for an Agricultural Contracting and Earthmoving Company

We need a business card for a new business based in Kilmore, Victoria. We are a company that specialises in two areas the first is and Earthmoving company, we do large jobs such as soccer fields to small jobs such as house cuts and riding arena's, drainage, and dams. The other side of the business specialises in Agricultural improvements and hay contracting. We require a card to represent both sides of the business. Must have the following information: Dale Morcombe, 2741 Bracken Rd, Kilmore Victoria 3764, ph:03 5902 4638, mob: 0427 913 684, e-mail: dale@morcombeworks.com.au. Earthmoving and Agricultural Contracting.

Target Market(s)

Builder's, Council's, new home buyers, Farmers

Industry/Entity Type

House

Font styles to use
Sans Serif

Colors
ec2026
000000
5c5c5c
ffffff

Requirements
Must have
• Both facets of the business represented. Company logo

```html
<!DOCTYPE html>
<html lang="en">
<head>
<meta charset="utf-8">
<title>Morcombe Contracting – Business Card</title>
<link rel="stylesheet" href="https://fonts.googleapis.com/css2?family=Saira:wght@300;400;700&family=Arimo:wght@400&display=swap">
<style>
  :root {
    --brand-red: #ec2026;
    --red-deep: #b5121b;
    --red-mid: #d41a22;
    --ink-black: #000000;
    --card-black: #1f1f1f;
    --ink-grey: #5c5c5c;
    --text-dark: #2b2b2b;
    --paper-white: #ffffff;
    --card-white: #e9e9e9;
    --backdrop: #d6d3cf;
  }
  * { box-sizing: border-box; margin: 0; padding: 0; }
  html, body {
    width: 1200px; height: 900px; overflow: hidden;
    background: var(--backdrop);
  }
  .canvas { position: relative; width: 1200px; height: 900px; }
  .card {
    position: absolute; top: 301px;
    width: 520px; height: 298px;
    overflow: hidden;
    box-shadow: 0 10px 28px rgba(0,0,0,.22);
  }
  .card--front { left: 60px; background: var(--card-black); }
  .card--back { left: 620px; background: var(--card-white); }

  .card__band {
    position: absolute; left: 0; bottom: 0;
    width: 520px; height: 40px; display: block;
  }

  /* front */
  .front__brand {
    position: absolute; left: 0; right: 0; top: 88px;
    display: flex; flex-direction: column; align-items: center;
  }
  .brand-mark {
    width: 34px; height: 34px; background: var(--brand-red);
    margin-bottom: 16px;
  }
  .front__name {
    font-family: "Saira", sans-serif; font-weight: 700;
    font-size: 30px; letter-spacing: 1px;
    color: var(--brand-red); text-transform: uppercase;
  }
  .front__tagline {
    margin-top: 8px;
    font-family: "Arimo", sans-serif; font-size: 14px;
    color: var(--paper-white);
  }

  /* back */
  .back__brand {
    position: absolute; right: 34px; top: 36px;
    display: flex; align-items: center; gap: 10px;
  }
  .back__brand .brand-mark { width: 18px; height: 18px; margin: 0; }
  .back__brand-name {
    font-family: "Saira", sans-serif; font-weight: 700;
    font-size: 16px; letter-spacing: .5px;
    color: var(--text-dark); text-transform: uppercase;
  }
  .contact {
    position: absolute; left: 34px; top: 128px;
    font-family: "Saira", sans-serif; color: var(--text-dark);
  }
  .contact__name {
    font-weight: 300; font-size: 24px; letter-spacing: 1px;
    text-transform: uppercase; margin-bottom: 10px;
  }
  .contact__list { list-style: none; }
  .contact__list li {
    font-family: "Arimo", sans-serif; font-size: 13px; line-height: 18px;
  }
  .contact__label {
    display: inline-block; width: 18px;
    color: var(--brand-red);
  }
  .contact__address {
    margin-top: 10px; margin-left: 18px;
    font-family: "Arimo", sans-serif; font-size: 13px;
  }
</style>
</head>
<body>
<main class="canvas">

  <section class="card card--front" aria-label="Business card front">
    <div class="front__brand">
      <span class="brand-mark" aria-hidden="true"></span>
      <h1 class="front__name">Morcombe Contracting</h1>
      <p class="front__tagline">Earthmoving and Agricultural Contracting</p>
    </div>
    <svg class="card__band" viewBox="0 0 520 40" aria-hidden="true">
      <rect x="0" y="6" width="520" height="2" fill="var(--paper-white)"/>
      <rect x="0" y="12" width="520" height="28" fill="var(--brand-red)"/>
      <polygon points="0,12 140,12 90,40 0,40" fill="var(--red-deep)"/>
      <polygon points="230,12 330,12 290,40 200,40" fill="var(--red-mid)"/>
      <polygon points="420,12 520,12 520,40 380,40" fill="var(--red-deep)"/>
    </svg>
  </section>

  <section class="card card--back" aria-label="Business card back">
    <div class="back__brand">
      <span class="brand-mark" aria-hidden="true"></span>
      <span class="back__brand-name">Morcombe Contracting</span>
    </div>
    <div class="contact">
      <h2 class="contact__name">Dale Morcombe</h2>
      <ul class="contact__list">
        <li><span class="contact__label">T</span>03 5902 4638</li>
        <li><span class="contact__label">M</span>0427 913 684</li>
        <li><span class="contact__label">E</span>dale@morcombeworks.com.au</li>
      </ul>
      <p class="contact__address">2741 Bracken Rd, Bellgrove Victoria 3791</p>
    </div>
    <svg class="card__band" viewBox="0 0 520 40" aria-hidden="true">
      <rect x="0" y="14" width="520" height="26" fill="var(--brand-red)"/>
      <polygon points="0,14 120,14 70,40 0,40" fill="var(--red-deep)"/>
      <polygon points="250,14 350,14 310,40 220,40" fill="var(--red-mid)"/>
      <polygon points="430,14 520,14 520,40 400,40" fill="var(--red-deep)"/>
    </svg>
  </section>

</main>
</body>
</html>
```